Halloway Consulting Cover 2 - Smart Capital

Halloway Consulting is a business consulting firm. We will publish a series of four thought leadership pieces online and via PDF. The second of the series is attached to this project. We need an eye-catching cover page with a back page that keeps with our branding. The document attached is in the final draft, and the cover and pack pages are placeholders only. You can find more about our branding and style on our website www.hallowayconsulting.com.au. The other three projects can be found here with a similar brief, and you are welcome to submit a design for all 4.

```html
<!DOCTYPE html>
<html lang="en">
<head>
<meta charset="utf-8">
<title>Halloway Consulting – Cover and Back Page</title>
<link rel="stylesheet" href="https://fonts.googleapis.com/css2?family=Bebas+Neue&family=Catamaran:wght@400;500;700;800&display=swap">
<style>
  :root {
    --canvas: #e8e8e8;
    --paper: #f7f9fb;
    --orange: #f7921e;
    --blue: #06aeef;
    --blue-deep: #0598d3;
    --ink: #111418;
    --photo-light: #f6f8fa;
    --photo-mid: #dfe5ea;
  }
  * { box-sizing: border-box; margin: 0; padding: 0; }
  html, body { width: 1200px; height: 870px; overflow: hidden; background: var(--canvas); }
  body { position: relative; font-family: "Catamaran", sans-serif; color: var(--ink); }

  .page {
    position: absolute; top: 70px; width: 520px; height: 736px;
    background: var(--paper); overflow: hidden;
  }
  .page--cover { left: 57px; }
  .page--back { left: 611px; }

  .page__photo {
    position: absolute; left: 0; top: 0; width: 324px; height: 100%;
    background:
      linear-gradient(200deg, rgba(255,255,255,0.9) 0%, rgba(255,255,255,0.4) 45%, rgba(255,255,255,0) 100%),
      linear-gradient(180deg, var(--photo-light) 0%, #eef2f5 55%, var(--photo-mid) 100%);
  }
  .page__band {
    position: absolute; right: 0; top: 0; width: 196px; height: 100%;
    background: linear-gradient(180deg, var(--blue) 0%, var(--blue-deep) 50%, var(--blue) 100%);
  }

  .brand { position: absolute; left: 36px; top: 62px; display: flex; align-items: center; gap: 12px; }
  .brand__dot { width: 52px; height: 52px; border-radius: 50%; background: var(--orange); }
  .brand__name {
    font-weight: 800; font-size: 22px; line-height: 20px; color: var(--blue);
  }

  .headline {
    position: absolute; left: 35px; top: 152px; width: 280px;
    font-family: "Bebas Neue", sans-serif; font-weight: 400; font-size: 63px; line-height: 59px;
    color: var(--orange); letter-spacing: 0; white-space: nowrap;
  }
  .headline__accent { color: var(--blue); }

  .cover__rule { position: absolute; left: 43px; top: 401px; width: 2px; height: 282px; background: var(--orange); }
  .cover__site { position: absolute; left: 43px; top: 689px; font-weight: 700; font-size: 15.5px; }

  .back__pitch {
    position: absolute; left: 31px; top: 176px; width: 300px;
    font-size: 17px; line-height: 22.5px; font-weight: 500; text-transform: uppercase;
  }
  .back__pitch strong { color: var(--orange); font-weight: 700; }
  .back__rule { position: absolute; left: 31px; top: 277px; width: 41px; height: 3px; background: var(--orange); }

  .contact { position: absolute; left: 31px; font-size: 11.5px; line-height: 15px; }
  .contact--first { top: 314px; }
  .contact--second { top: 404px; left: 34px; }
  .contact__name { font-weight: 800; font-size: 18px; line-height: 20px; color: var(--blue); }
  .contact__role { color: var(--orange); margin-bottom: 6px; }
  .contact b { font-weight: 800; }

  .follow { position: absolute; left: 34px; top: 578px; display: flex; align-items: center; gap: 5px; font-size: 17px; }
  .follow__icon { width: 18px; height: 18px; border-radius: 50%; }
  .follow__icon--blue { background: var(--blue); margin-left: 3px; }
  .follow__icon--dark { background: var(--ink); }
  .back__site { position: absolute; left: 34px; top: 598px; font-weight: 800; font-size: 16px; color: var(--orange); }
</style>
</head>
<body>
  <section class="page page--cover">
    <div class="page__photo" role="img" aria-label="Faded upward view of office towers and a street lamp"></div>
    <div class="page__band" role="img" aria-label="Blue geometric maze pattern band"></div>
    <div class="brand">
      <span class="brand__dot"></span>
      <span class="brand__name">Halloway<br>Consulting</span>
    </div>
    <h1 class="headline">Chasing<br>cash like<br>Bruin <span class="headline__accent">chases</span><br><span class="headline__accent">the Wumple</span></h1>
    <div class="cover__rule"></div>
    <p class="cover__site">hallowayconsulting.com.au</p>
  </section>

  <section class="page page--back">
    <div class="page__photo" role="img" aria-label="Faded upward view of office towers"></div>
    <div class="page__band" role="img" aria-label="Blue geometric maze pattern band"></div>
    <div class="brand">
      <span class="brand__dot"></span>
      <span class="brand__name">Halloway<br>Consulting</span>
    </div>
    <p class="back__pitch">Contact us to find out how Halloway Consulting can help build your company into a market <strong>leader today.</strong></p>
    <div class="back__rule"></div>

    <div class="contact contact--first">
      <p class="contact__name">Daniel Halloway</p>
      <p class="contact__role">Managing Director</p>
      <p><b>Mobile</b> +61 400 555 018</p>
      <p><b>Email</b> daniel@hallowayconsulting.com.au</p>
    </div>
    <div class="contact contact--second">
      <p class="contact__name">Marcus Halloway</p>
      <p class="contact__role">Managing Director</p>
      <p><b>Mobile</b> +61 400 555 027</p>
      <p><b>Email</b> marcus@hallowayconsulting.com.au</p>
    </div>

    <div class="follow">
      <span>Follow</span>
      <span class="follow__icon follow__icon--blue"></span>
      <span class="follow__icon follow__icon--dark"></span>
    </div>
    <p class="back__site">hallowayconsulting.com.au</p>
  </section>
</body>
</html>
```